Business Card for a Wedding Films Business

We require a business card design for our business 'Lewis Marrow Wedding Films'. The logo needs to look classy and high end.

Target Market(s)

Wedding Couples

Contact Information for Business Card

Lewis Marrow Wedding Films
07312 605 227
films@lewismarrowreels.com
www.lewismarrowreels.com

Facebook: @lewismarrowweddingfilms
Instagram: @lewismarrowfilms

Font styles to use
Sans Serif

Requirements
Must have
• Social media icons - Facebook and Instagram

```html
<!DOCTYPE html>
<html lang="en">
<head>
<meta charset="utf-8">
<title>Lewis Marrow Wedding Films – Business Card</title>
<link href="https://fonts.googleapis.com/css2?family=Roboto:wght@400;500&display=swap" rel="stylesheet">
<style>
  :root {
    --backdrop: #d8d2d5;
    --card: #0a1320;
    --ink: #ffffff;
    --ink-soft: #e8ebf0;
    --branch-tone: #f4f4f4;
  }
  * { margin: 0; padding: 0; box-sizing: border-box; }
  html, body {
    width: 1200px;
    height: 1028px;
    overflow: hidden;
    background: var(--backdrop);
  }
  .stage {
    width: 1200px;
    height: 1028px;
    display: flex;
    align-items: center;
    justify-content: center;
  }
  .card {
    position: relative;
    width: 1000px;
    height: 636px;
    background: var(--card);
    font-family: "Roboto", sans-serif;
    color: var(--ink);
    overflow: hidden;
  }
  .brand {
    position: absolute;
    left: 110px;
    top: 215px;
    display: flex;
    align-items: center;
    gap: 22px;
  }
  .brand-mark {
    width: 58px;
    height: 58px;
    border: 3px solid var(--ink);
  }
  .brand-name {
    font-weight: 400;
    font-size: 30px;
    letter-spacing: 6px;
    line-height: 1.3;
    text-transform: uppercase;
    color: var(--ink);
  }
  .brand-name span { display: block; font-size: 16px; letter-spacing: 7px; }
  .branch {
    position: absolute;
    left: 520px;
    top: 90px;
    width: 180px;
    height: 546px;
    background: linear-gradient(180deg, rgba(244,244,244,0.18), rgba(244,244,244,0.35));
    border-radius: 90px 90px 0 0;
  }
  .contact {
    position: absolute;
    left: 690px;
    top: 120px;
    width: 290px;
    text-align: center;
    font-size: 21px;
    line-height: 1.3;
    color: var(--ink-soft);
  }
  .contact-name { font-weight: 500; color: var(--ink); }
  .social { margin-top: 28px; }
  .social-icon {
    display: block;
    margin: 0 auto 6px;
    width: 26px;
    height: 26px;
    border-radius: 50%;
    background: var(--ink);
  }
</style>
</head>
<body>
  <main class="stage">
    <section class="card">
      <div class="brand">
        <div class="brand-mark"></div>
        <div class="brand-name">Lewis Marrow<span>Wedding Films</span></div>
      </div>

      <div class="branch" role="img" aria-label="White illustration of a slender berry branch rising from the bottom edge"></div>

      <div class="contact">
        <p class="contact-name">Lewis Marrow Wedding Films</p>
        <p>07312 605 227</p>
        <p>films@lewismarrowreels.com</p>
        <p>www.lewismarrowreels.com</p>

        <div class="social">
          <span class="social-icon"></span>
          <p>@lewismarrowweddingfilms</p>
        </div>
        <div class="social">
          <span class="social-icon"></span>
          <p>@lewismarrowfilms</p>
        </div>
      </div>
    </section>
  </main>
</body>
</html>
```